Business Card Design Project

I have had my current business card for 6years and it is time to upgrade my business card. I have uploaded my old card
I am a retail specialty shop designer and want something designer looking but professional.
Target Market(s)
30-60 year old people in retail businesses
Industry/Entity Type
Retail
Requirements
Must have
- The Vela Fitouts logo (but colour can and style can be altered)
My name, position and contact details as per my existing card attached .
Rupert Calloway Director
m: 0418536771
rupert@velafitouts.com.au
www.velafitouts.com.au
t:02 94417268 f: 02 94417293
po box 817 wattlebrook nsw 1482
Nice to have
- Use both sides of the card

```html
<!DOCTYPE html>
<html lang="en">
<head>
<meta charset="utf-8">
<title>Vela Fitouts – Business Card</title>
<link rel="stylesheet" href="https://fonts.googleapis.com/css2?family=Open+Sans:wght@400;600&display=swap">
<style>
  :root {
    --backdrop: #8c8c8e;
    --amber-light: #fdc634;
    --amber-deep: #f6a623;
    --charcoal-light: #505053;
    --charcoal-deep: #333335;
    --ink-dark: #3a3a3c;
    --ink-light: #f4f4f4;
    --edge: #ffffff;
  }
  * { box-sizing: border-box; margin: 0; padding: 0; }
  html, body {
    width: 1200px;
    height: 902px;
    overflow: hidden;
  }
  body {
    position: relative;
    background: var(--backdrop);
    font-family: "Open Sans", Arial, sans-serif;
  }
  .card {
    position: absolute;
    top: 116px;
    width: 396px;
    height: 682px;
    border: 2px solid var(--edge);
    box-shadow: 0 4px 14px rgba(0, 0, 0, 0.35);
  }
  .card--front {
    left: 164px;
    background: radial-gradient(circle at 50% 40%, var(--amber-light) 0%, var(--amber-deep) 80%);
    color: var(--ink-dark);
  }
  .card--back {
    left: 646px;
    background: radial-gradient(circle at 50% 30%, var(--charcoal-light) 0%, var(--charcoal-deep) 85%);
    color: var(--ink-light);
  }
  .brand {
    position: absolute;
    top: 115px;
    left: 0;
    width: 100%;
    height: 183px;
    display: flex;
    flex-direction: column;
    align-items: center;
    justify-content: center;
    gap: 22px;
  }
  .brand__square {
    width: 72px;
    height: 72px;
  }
  .card--front .brand__square { background: var(--ink-dark); }
  .card--back .brand__square { background: var(--amber-light); }
  .brand__name {
    font-size: 30px;
    font-weight: 400;
    letter-spacing: 3px;
    text-transform: uppercase;
  }
  .card--back .brand__name { color: var(--ink-light); }
  .person {
    position: absolute;
    top: 384px;
    width: 100%;
    text-align: center;
  }
  .person__name {
    font-size: 28px;
    font-weight: 400;
    letter-spacing: 2.5px;
    text-transform: uppercase;
  }
  .person__role {
    margin-top: 4px;
    font-size: 18px;
    letter-spacing: 8px;
    text-transform: uppercase;
  }
  .direct-contact {
    position: absolute;
    top: 583px;
    width: 100%;
    text-align: center;
    font-size: 19px;
    line-height: 27px;
  }
  .direct-contact__mobile { letter-spacing: 4px; }
  .office-contact {
    position: absolute;
    top: 530px;
    left: 46px;
    font-size: 19px;
    line-height: 27px;
    color: var(--ink-light);
  }
  .office-contact__web { letter-spacing: 2.5px; }
  .office-contact__phone { letter-spacing: 6.5px; }
</style>
</head>
<body>
  <section class="card card--front" aria-label="Card front">
    <div class="brand">
      <div class="brand__square"></div>
      <div class="brand__name">Vela Fitouts</div>
    </div>
    <div class="person">
      <p class="person__name">Rupert Calloway</p>
      <p class="person__role">Director</p>
    </div>
    <div class="direct-contact">
      <p class="direct-contact__mobile">m: 0418536771</p>
      <p class="direct-contact__email">rupert@velafitouts.com.au</p>
    </div>
  </section>

  <section class="card card--back" aria-label="Card back">
    <div class="brand">
      <div class="brand__square"></div>
      <div class="brand__name">Vela Fitouts</div>
    </div>
    <div class="office-contact">
      <p class="office-contact__web">www.velafitouts.com.au</p>
      <p class="office-contact__phone">t:(02)94417268</p>
      <p class="office-contact__phone">f:(02)94417293</p>
      <p class="office-contact__post">po box 817. wattlebrook nsw 1482</p>
    </div>
  </section>
</body>
</html>
```